Need a Facebook design page for our site join the lumivera

the website is jointhelumivera (dot) com

The site is about helping people get into modelling. they sign up on the site we give them a call if we think they have potential to become a model. We are looking for a design for our Facebook page we want the design to be as stunning as the website is.

Target Market(s)

People who want to become models

Industry/Entity Type

Call

Font styles to use
Sans Serif

Requirements
Must have
• Must look like the website
Nice to have
• Would like to it to look and have the same theme as the facebook

```html
<!DOCTYPE html>
<html lang="en">
<head>
<meta charset="utf-8">
<title>Join the Lumivera – Facebook Cover</title>
<link rel="stylesheet" href="https://fonts.googleapis.com/css2?family=Roboto+Condensed:wght@500;700&display=swap">
<style>
  :root {
    --ink-dark: #141414;
    --ink-mid: #3a3836;
    --ink-warm: #5a544c;
    --lens-red: #7a1a10;
    --gold: #c9a24a;
    --white: #ffffff;
    --frame: rgba(255, 255, 255, 0.55);
  }
  * { margin: 0; padding: 0; box-sizing: border-box; }
  html, body {
    width: 1200px;
    height: 628px;
    overflow: hidden;
    background: var(--ink-dark);
  }
  .cover {
    position: relative;
    width: 1200px;
    height: 628px;
    overflow: hidden;
  }
  .cover__backdrop {
    position: absolute;
    inset: 0;
    background:
      radial-gradient(circle at 760px 400px, rgba(180, 40, 20, 0.55) 0, rgba(122, 26, 16, 0.25) 40px, transparent 110px),
      radial-gradient(ellipse 420px 320px at 820px 330px, rgba(90, 84, 76, 0.65), transparent 75%),
      radial-gradient(ellipse 520px 360px at 1060px 200px, rgba(150, 145, 138, 0.35), transparent 70%),
      radial-gradient(ellipse 700px 500px at 300px 250px, rgba(58, 56, 54, 0.8), transparent 80%),
      linear-gradient(180deg, #2b2a28 0%, #1c1b1a 60%, #121212 100%);
  }
  .cover__backdrop::after {
    content: "";
    position: absolute;
    inset: 0;
    background: rgba(0, 0, 0, 0.28);
  }
  .cover__content {
    position: relative;
    z-index: 1;
    width: 100%;
    height: 100%;
    text-align: center;
  }
  .headline {
    position: absolute;
    top: 102px;
    left: 0;
    right: 0;
    font-family: "Roboto Condensed", "Arial Narrow", sans-serif;
    font-weight: 700;
    font-size: 55px;
    line-height: 83px;
    letter-spacing: 0.5px;
    color: var(--gold);
    text-shadow: 0 2px 6px rgba(0, 0, 0, 0.5);
  }
  .cta {
    position: absolute;
    left: 416px;
    top: 324px;
    width: 382px;
    height: 85px;
    border: 1.5px solid var(--frame);
    display: flex;
    align-items: center;
    justify-content: center;
    font-family: "Roboto Condensed", "Arial Narrow", sans-serif;
    font-weight: 500;
    font-size: 29px;
    letter-spacing: 0.4px;
    color: var(--white);
    text-decoration: none;
  }
  .contact {
    position: absolute;
    left: 0;
    right: 0;
    font-family: "Roboto Condensed", "Arial Narrow", sans-serif;
    font-weight: 700;
    font-size: 29px;
    letter-spacing: 0.4px;
    color: var(--white);
  }
  .contact--email { top: 458px; }
  .contact--web { top: 522px; }
</style>
</head>
<body>
  <main class="cover">
    <div class="cover__backdrop" role="img" aria-label="Dark, warm-toned close-up photograph of a camera lens with a red glint, on a blurred background"></div>
    <div class="cover__content">
      <h1 class="headline">Join the lumivera helps aspiring<br>models break into the modelling world</h1>
      <a class="cta" href="#">REGISTER YOURSELF</a>
      <p class="contact contact--email">ENQUIRIES@JOINTHELUMIVERA.COM</p>
      <p class="contact contact--web">WWW.JOINTHELUMIVERA.COM</p>
    </div>
  </main>
</body>
</html>
```